political campaign tax exemption on school taxes that dont have kids in the district

Harlow Vale School Board Races

Taxes, Taxes, Taxes!
Everyone pays them!
You have tax exemption for the elderly.
You have tax exemption for the veterans.
What about tax exemptions for you?

In Texas, a governing entity, has the option of giving a 20 percent tax exemption. Our current school board, hasnt offered it you! We will!

Can we count on your vote? You can count on ours!
small discloure (political ad paid by candidates)

attached are the candidates for this exemption

Political

• need to include disclaimer at bottom.

political ad paid by candidate

```html
<!DOCTYPE html>
<html lang="en">
<head>
<meta charset="utf-8">
<title>Taxes, Taxes, Taxes! — Harlow Vale School Board Races</title>
<link rel="stylesheet" href="https://fonts.googleapis.com/css2?family=Bebas+Neue&display=swap">
<style>
  :root {
    --campaign-red: #ed1c24;
    --campaign-blue: #2b3a97;
    --sky-blue: #2a3f9b;
    --sky-blue-deep: #3a2f8c;
    --ink-white: #ffffff;
  }
  html, body {
    margin: 0;
    padding: 0;
    overflow: hidden;
    background: var(--campaign-red);
  }
  .flyer {
    position: relative;
    width: 1200px;
    height: 928px;
    overflow: hidden;
    background: var(--campaign-red);
    font-family: "Bebas Neue", "Arial Narrow", sans-serif;
    color: var(--ink-white);
    text-transform: uppercase;
  }
  .backdrop {
    position: absolute;
    inset: 0;
    width: 1200px;
    height: 928px;
  }
  .headline {
    position: absolute;
    left: 0;
    top: 30px;
    margin: 0;
    font-weight: 400;
    font-size: 114px;
    line-height: 116px;
    letter-spacing: 1px;
  }
  .headline span { display: block; }
  .headline .line-1 { padding-left: 63px; }
  .headline .line-2 { padding-left: 158px; }
  .headline .line-3 { padding-left: 234px; }

  .exemptions {
    position: absolute;
    left: 63px;
    top: 396px;
    margin: 0;
    font-size: 44px;
    line-height: 40px;
    letter-spacing: 2px;
  }
  .exemptions p { margin: 0; }
  .exemptions .question {
    font-size: 64px;
    line-height: 60px;
    letter-spacing: 1px;
    margin-top: 8px;
  }

  .vote-call {
    position: absolute;
    left: 62px;
    top: 644px;
    margin: 0;
    font-size: 61px;
    line-height: 62px;
    color: var(--campaign-blue);
  }

  .promise {
    position: absolute;
    left: 63px;
    top: 734px;
    margin: 0;
    font-size: 37px;
    line-height: 32px;
    letter-spacing: 1.5px;
  }

  .disclaimer {
    position: absolute;
    left: 63px;
    bottom: 22px;
    margin: 0;
    font-size: 20px;
    line-height: 22px;
    letter-spacing: 1px;
  }
</style>
</head>
<body>
  <main class="flyer">
    <svg class="backdrop" viewBox="0 0 1200 928">
      <defs>
        <linearGradient id="sky-gradient" x1="0" y1="0" x2="1" y2="0">
          <stop offset="0" stop-color="#3a2f8c"/>
          <stop offset="0.35" stop-color="#2a3f9b"/>
          <stop offset="1" stop-color="#2a3f9b"/>
        </linearGradient>
        <linearGradient id="burden-gradient" x1="0" y1="0" x2="0" y2="1">
          <stop offset="0" stop-color="#ffffff"/>
          <stop offset="0.45" stop-color="#f08a8e"/>
          <stop offset="1" stop-color="#ed1c24"/>
        </linearGradient>
      </defs>
      <path class="sky" d="M366 0 L1200 0 L1200 480 L1060 440 L900 428 L760 440 Q600 250 366 0 Z" fill="url(#sky-gradient)"/>
      <rect class="tax-burden-illustration" x="758" y="52" width="410" height="384" rx="6"
            fill="url(#burden-gradient)" role="img"
            aria-label="Illustration of two businessmen straining to carry a heavy TAX block up a hill"/>
    </svg>

    <h1 class="headline">
      <span class="line-1">Taxes,</span>
      <span class="line-2">Taxes,</span>
      <span class="line-3">Taxes!</span>
    </h1>

    <section class="exemptions">
      <p>Everyone pays them!</p>
      <p>You have tax exemption for the elderly.</p>
      <p>You have tax exemption for the veterans</p>
      <p class="question">What about tax exemptions for you?</p>
    </section>

    <p class="vote-call">Can we count on your vote? You can count on ours!</p>

    <p class="promise">
      In Texas, a governing entity, has the option of giving<br>
      a 20 percent tax exemption. Our current school board,<br>
      hasnt offered it you! We will!
    </p>

    <p class="disclaimer">Political ad paid by candidates · Harlow Vale School Board Races</p>
  </main>
</body>
</html>
```